Company website design for Brindlemoor Valuation Advisory LLC

Design of company website. See uploaded outline. Logo hex codes for the icon colors: middle blue - 4D6C8A, dark blue - 11122B.

```html
<!DOCTYPE html>
<html lang="en">
<head>
<meta charset="utf-8">
<title>Brindlemoor Valuation Advisory LLC</title>
<link rel="stylesheet" href="https://fonts.googleapis.com/css2?family=Outfit:wght@300;400;500;600&display=swap">
<style>
:root{
  --blue:#4D6C8A;
  --navy:#11122B;
  --white:#FFFFFF;
  --paper:#FFFFFF;
  --ink:#1d1e2c;
  --muted:#8a8f99;
  --line:#e3e5ea;
}
*{box-sizing:border-box;margin:0;padding:0}
html,body{width:1200px;height:3736px;overflow:hidden;background:var(--paper)}
body{position:relative;font-family:"Outfit",sans-serif;color:var(--ink)}
.abs{position:absolute}

/* brand sheet */
.brand-row{top:88px;left:0;width:1200px;height:70px}
.brand-lock{left:277px;top:8px;display:flex;align-items:center;gap:10px}
.brand-lock .sq{width:44px;height:44px;background:var(--navy)}
.brand-name{font-size:31px;font-weight:400;color:var(--navy);letter-spacing:.5px;line-height:1}
.brand-sub{font-size:11px;letter-spacing:1.6px;color:var(--navy);margin-top:4px}
.divider{width:1px;height:60px;background:var(--line);top:2px}
.spec{top:12px;font-size:15px;color:var(--navy)}
.spec b{display:block;font-weight:600;margin-bottom:6px}
.swatches{display:flex;gap:8px;margin-top:4px}
.swatches i{width:25px;height:25px;border-radius:6px;display:block}

/* site */
.site{left:69px;top:800px;width:1057px;height:2810px;background:var(--white);box-shadow:0 0 12px rgba(0,0,0,.08)}
.site-header{left:0;top:0;width:1057px;height:79px;display:flex;align-items:center;justify-content:space-between;padding:0 78px}
.site-header .brand-name{font-size:30px}
.menu-btn{width:30px;height:30px;border-radius:5px;background:var(--navy);display:flex;flex-direction:column;justify-content:center;align-items:center;gap:4px}
.menu-btn i{width:16px;height:2px;background:#fff;display:block}

.photo{position:absolute;left:0;width:1057px}
.hero{top:79px;height:366px;background:linear-gradient(180deg,#3d4b57 0%,#4e5a55 35%,#2c3a33 60%,#29414a 100%);display:flex;flex-direction:column;align-items:center;justify-content:center;color:#fff;text-align:center}
.hero h1{font-size:40px;font-weight:500;line-height:1.1;margin-top:-20px}
.hero p{font-size:22px;font-weight:400;margin-top:4px;letter-spacing:.3px}

.values{top:445px;height:120px;background:var(--navy);text-align:center;color:#fff}
.values h2{font-size:23px;font-weight:300;color:var(--blue);margin-top:25px}
.values p{font-size:15px;margin-top:9px;letter-spacing:.3px}
.values p span{color:#5a5d70;margin:0 6px}

.what{top:565px;height:410px;width:1057px}
.sec-title{font-size:22px;font-weight:500;color:var(--blue)}
.what .sec-title{position:absolute;left:78px;top:68px}
.service{position:absolute;width:250px;display:flex;gap:10px}
.service svg{flex:none}
.service h3{font-size:13px;font-weight:600;color:var(--blue);letter-spacing:.4px;line-height:1.3;margin-bottom:5px}
.service p{font-size:11.5px;color:var(--muted);line-height:1.45}

.serve{top:975px;height:295px;background:var(--navy);color:#fff;text-align:center}
.serve .sec-title{margin-top:64px}
.serve-list{display:flex;justify-content:space-between;padding:0 97px;margin-top:30px}
.serve-item{width:175px;font-size:12px;line-height:1.45}
.serve-item svg{display:block;margin:0 auto 8px}

.road{top:1270px;height:359px;background:linear-gradient(180deg,#c8a57c 0%,#8a7566 22%,#3a4a44 45%,#2f3a34 70%,#3c423c 100%)}

.industries{top:1629px;width:1057px;height:300px;text-align:center}
.industries .sec-title{margin-top:64px}
.arrow-btn{position:absolute;top:183px;width:20px;height:20px;border:1.5px solid var(--navy);border-radius:5px;display:flex;align-items:center;justify-content:center}
.ind{position:absolute;top:123px;width:204px;text-align:center}
.ind .pic{width:204px;height:140px}
.ind span{display:block;font-size:14px;color:var(--navy);margin-top:10px;line-height:1.2}

.lake{top:2204px;height:314px;background:linear-gradient(180deg,#56616c 0%,#6c7470 35%,#3a4a3c 65%,#2c3a3a 100%)}
.inquiry{left:148px;top:1988px;width:762px;height:338px;background:#fff;box-shadow:0 2px 14px rgba(0,0,0,.08);text-align:center}
.inquiry .sec-title{margin-top:50px}
.field{position:absolute;border:1px solid var(--line);font-size:10px;color:var(--muted);padding:8px 13px;text-align:left}
.submit{position:absolute;left:330px;top:257px;width:101px;height:28px;background:var(--blue);color:#fff;font-size:12px;border-radius:2px;line-height:28px}

.contact{top:2518px;width:1057px;height:253px;text-align:center}
.contact .sec-title{margin-top:68px}
.c-box{position:absolute;top:112px;width:266px;height:76px;box-shadow:0 0 10px rgba(0,0,0,.07);display:flex;align-items:center;justify-content:center;gap:12px;font-size:13px;color:var(--navy);text-align:left;line-height:1.35}

.footer{left:0;top:2771px;width:1057px;height:39px;background:var(--navy);color:#fff;font-size:10px;display:flex;align-items:center;justify-content:space-between;padding:0 78px}
.footer nav a{color:#fff;text-decoration:none;margin-left:20px}
</style>
</head>
<body>

<section class="abs brand-row">
  <div class="abs brand-lock">
    <span class="sq"></span>
    <div>
      <div class="brand-name">BRINDLEMOOR</div>
      <div class="brand-sub">VALUATION ADVISORY LLC</div>
    </div>
  </div>
  <span class="abs divider" style="left:556px"></span>
  <div class="abs spec" style="left:610px"><b>Fonts:</b>Outfit</div>
  <span class="abs divider" style="left:770px"></span>
  <div class="abs spec" style="left:824px;top:4px"><b>Colors:</b>
    <div class="swatches"><i style="background:var(--blue)"></i><i style="background:var(--navy)"></i><i style="background:#fff;border:1px solid #eee"></i></div>
  </div>
</section>

<main class="abs site">
  <header class="abs site-header">
    <div style="display:flex;align-items:center;gap:10px">
      <span class="sq" style="width:44px;height:44px;background:var(--navy);display:block"></span>
      <div>
        <div class="brand-name">BRINDLEMOOR</div>
        <div class="brand-sub">VALUATION ADVISORY LLC</div>
      </div>
    </div>
    <div class="menu-btn"><i></i><i></i><i></i></div>
  </header>

  <section class="photo hero" role="img" aria-label="Mountain lake with pine forest and rocky peaks">
    <h1>Building a Business is a Journey</h1>
    <p>We have the valuation expertise to guide you.</p>
  </section>

  <section class="photo values">
    <h2>Our Values</h2>
    <p>INTEGRITY<span>|</span>RESPONSIVENESS<span>|</span>EXCELLENCE<span>|</span>RELATIONSHIPS<span>|</span>COMMUNITY</p>
  </section>

  <section class="abs what">
    <h2 class="sec-title">What We Do</h2>
    <div class="service" style="left:330px;top:66px;width:300px">
      <svg width="44" height="46" viewBox="0 0 44 46" fill="none" stroke="#4D6C8A" stroke-width="1.5"><path d="M4 2h26l10 10v32H4z"/><path d="M30 2v10h10"/><rect x="7" y="10" width="16" height="9"/><path d="M12 28h22M12 33h22M12 38h22M8 28h1M8 33h1M8 38h1"/></svg>
      <div><h3>TAX-RELATED VALUATIONS</h3><p>Valuations for estate/gift tax, charitable contributions, equity-linked compensation, corporate restructuring and insolvency purposes.</p></div>
    </div>
    <div class="service" style="left:676px;top:66px;width:300px">
      <svg width="44" height="46" viewBox="0 0 44 46" fill="none" stroke="#4D6C8A" stroke-width="1.5"><rect x="3" y="3" width="28" height="38"/><path d="M9 30v-6M15 30V16M21 30v-10"/><circle cx="32" cy="32" r="7"/><path d="M37 37l5 5"/></svg>
      <div><h3>FINANCIAL REPORTING</h3><p>Our work includes purchase price allocations, fresh-start accounting, impairment analyses, equity-linked compensation, leases and financial instruments.</p></div>
    </div>
    <div class="service" style="left:330px;top:202px;width:300px">
      <svg width="44" height="46" viewBox="0 0 44 46" fill="none" stroke="#4D6C8A" stroke-width="1.5"><rect x="26" y="4" width="12" height="14"/><path d="M32 7v8"/><circle cx="14" cy="24" r="6"/><path d="M3 42c0-7 5-11 11-11s11 4 11 11"/><path d="M28 40v-8M33 40v-12M38 40v-6"/></svg>
      <div><h3>FINANCING &amp; TRANSACTION ADVISORY</h3><p>Financial assessments to evaluate debt structure and capital adequacy. Valuation support for loan underwriting, capital raises, share redemptions, minority interest buyouts, buy-sell agreements as well as for mergers, acquisitions and divestitures.</p></div>
    </div>
    <div class="service" style="left:676px;top:202px;width:300px">
      <svg width="44" height="46" viewBox="0 0 44 46" fill="none" stroke="#4D6C8A" stroke-width="1.5"><rect x="14" y="4" width="16" height="9" rx="2"/><rect x="14" y="19" width="16" height="9" rx="2"/><rect x="14" y="34" width="16" height="9" rx="2"/><path d="M14 8H5v15h9M30 23h9v15h-9"/></svg>
      <div><h3>BUSINESS PLANNING &amp; ADVISORY</h3><p>Outsourced financial planning and analysis (FP&amp;A) services, including model development, strategy valuation and exit options analysis.</p></div>
    </div>
  </section>

  <section class="photo serve">
    <h2 class="sec-title">Who Do We Serve</h2>
    <div class="serve-list">
      <div class="serve-item"><svg width="46" height="46" viewBox="0 0 46 46" fill="none" stroke="#fff" stroke-width="1.4"><circle cx="16" cy="13" r="7"/><circle cx="31" cy="13" r="7"/><path d="M4 42c0-9 5-15 12-15s12 6 12 15M22 30c2-2 5-3 9-3 7 0 11 6 11 15"/></svg>Closely-Held / Family-Owned Businesses</div>
      <div class="serve-item"><svg width="46" height="46" viewBox="0 0 46 46" fill="none" stroke="#fff" stroke-width="1.4"><rect x="6" y="18" width="24" height="24"/><path d="M11 24h4M21 24h4M11 30h4M21 30h4M15 42v-6h6v6"/><circle cx="35" cy="12" r="7"/><path d="M35 8v8"/></svg>Private-Equity Sponsored Companies</div>
      <div class="serve-item"><svg width="46" height="46" viewBox="0 0 46 46" fill="none" stroke="#fff" stroke-width="1.4"><path d="M4 42h38M8 42V30h6v12M18 42V24h6v12M28 42V18h6v24M36 42V12h6v30"/><path d="M6 24l10-8 8 4 16-14"/></svg>Publicly Traded Companies</div>
      <div class="serve-item"><svg width="46" height="46" viewBox="0 0 46 46" fill="none" stroke="#fff" stroke-width="1.4"><path d="M4 16L23 5l19 11z"/><path d="M6 16h34M9 20v16M17 20v16M29 20v16M37 20v16M4 40h38"/></svg>Lenders</div>
    </div>
  </section>

  <section class="photo road" role="img" aria-label="Winding road through meadow toward snowy mountains at sunset"></section>

  <section class="abs industries">
    <h2 class="sec-title">Industries Served</h2>
    <span class="arrow-btn" style="left:44px"><svg width="10" height="10" viewBox="0 0 10 10" fill="none" stroke="#11122B" stroke-width="1.4"><path d="M9 5H1M4 2L1 5l3 3"/></svg></span>
    <span class="arrow-btn" style="left:993px"><svg width="10" height="10" viewBox="0 0 10 10" fill="none" stroke="#11122B" stroke-width="1.4"><path d="M1 5h8M6 2l3 3-3 3"/></svg></span>
    <div class="ind" style="left:78px"><div class="pic" role="img" aria-label="Digital network technology graphic" style="background:linear-gradient(135deg,#0d2c5c,#2a6fb0)"></div><span>Technology</span></div>
    <div class="ind" style="left:310px"><div class="pic" role="img" aria-label="Engineers in hard hats at a factory" style="background:linear-gradient(135deg,#2b3d52,#c9c23a)"></div><span>Manufacturing</span></div>
    <div class="ind" style="left:543px"><div class="pic" role="img" aria-label="Warehouse shelves with pallet jack" style="background:linear-gradient(180deg,#8a6e4e,#c9c6c0)"></div><span>Wholesale / Distribution</span></div>
    <div class="ind" style="left:775px"><div class="pic" role="img" aria-label="Professionals meeting in an office" style="background:linear-gradient(135deg,#c7b3a2,#e4e1dc)"></div><span>Business &amp; Professional<br>Services</span></div>
  </section>

  <section class="photo lake" role="img" aria-label="Mountain lake shoreline with evergreen forest"></section>

  <section class="abs inquiry">
    <h2 class="sec-title">Quick Inquiry</h2>
    <div class="field" style="left:53px;top:97px;width:321px">First Name</div>
    <div class="field" style="left:387px;top:97px;width:321px">Last Name</div>
    <div class="field" style="left:53px;top:143px;width:321px">Email</div>
    <div class="field" style="left:387px;top:143px;width:321px;height:80px">Message</div>
    <div class="field" style="left:53px;top:189px;width:321px">Phone</div>
    <div class="submit">Submit</div>
  </section>

  <section class="abs contact">
    <h2 class="sec-title">Contact Info</h2>
    <div class="c-box" style="left:109px">
      <svg width="30" height="30" viewBox="0 0 30 30" fill="none" stroke="#4D6C8A" stroke-width="1.6"><path d="M15 22s7-7 7-12a7 7 0 0 0-14 0c0 5 7 12 7 12z"/><circle cx="15" cy="10" r="2.5"/><path d="M8 20l-6 8h26l-6-8"/></svg>
      <span>1820 W Alder Ridge Ct Ste 310,<br>Boise Valley, ID 83700</span></div>
    <div class="c-box" style="left:395px">
      <svg width="28" height="28" viewBox="0 0 28 28" fill="none" stroke="#4D6C8A" stroke-width="1.6"><path d="M5 3l5 1 2 6-3 2c1 3 4 6 7 7l2-3 6 2 1 5c-2 2-4 2-6 2C10 24 4 18 3 9c0-2 0-4 2-6z"/><path d="M16 4a8 8 0 0 1 8 8M16 8a4 4 0 0 1 4 4"/></svg>
      <span>+1 208 555 0142</span></div>
    <div class="c-box" style="left:681px">
      <svg width="28" height="28" viewBox="0 0 28 28" fill="none" stroke="#4D6C8A" stroke-width="1.8"><circle cx="14" cy="14" r="5"/><path d="M19 9v7c0 3 5 3 5-2a10 10 0 1 0-4 8"/></svg>
      <span>info@brindlemoorvaluation.com</span></div>
  </section>

  <footer class="abs footer">
    <span>Copyright © 2021 Corvessa Capital. All Rights Reserved</span>
    <nav><a href="#">Terms of Use</a><a href="#">Privacy Policy</a></nav>
  </footer>
</main>

</body>
</html>
```